Multi-purose Thank You Card Design Project (Real Estate)

We are in the business of listing and selling luxury homes in Atlanta Georgia and are the #1 Award Winning team in our office, #5 in Georgia and #5 in Southeast for all Brandt Halloway team. Your can learn more about us at www.marrowbyandpartners.example.

In our business model, growing a team to $80 million in sales (we will sell $40,000,000 in 2013 and are determined to grow rapidly while providing high levels of service) requires that we carefully nurture our sphere of influence database through multiple, high quality, well-designed touches like (thank you cards, letters, phone calls, gifts etc)

We need a thank you card:
1. Can be used for multiple purposes
a. Referral thank you.
b. House closing anniversary thank you
2. File built in Photoshop with layers that we can edit (we are proficient in Photoshop)
3. Design based on the Brandt Halloway luxury Style Guide but does not restrict your creativity. Break the rules and have more impact.
5. Card 7" w x 5' h opening at top
Updates

The first place payment guarantee has been increased by $100 to $320.

The attached logo files have been replaced and should open correctly.
Kindly,
Pelford

Target Market(s)

Buyers and Seller of Homes from $300k to $10m

Industry/Entity Type

Business

Requirements
Must have
• Copy on cover: "Thanks for the Referral"
Logo 1: Brandt Halloway Luxury Logo
File in 300 dpi for print
File in 96 dpi for use with Post Ahead Notes
Nice to have
• Photo of Home (optional)
Logo 2 Marrowby and Partners Logo (optional)

```html
<!DOCTYPE html>
<html lang="en">
<head>
<meta charset="utf-8">
<title>Thanks for the Referral Card</title>
<link rel="stylesheet" href="https://fonts.googleapis.com/css2?family=Pinyon+Script&family=Archivo:wght@500&display=swap">
<style>
  :root {
    --backdrop: #000000;
    --card-red: #c0001a;
    --tag-taupe: #8b8174;
    --tag-lime: #bfcb4c;
    --script-cream: #f4f1d2;
    --caption-ink: #111111;
  }
  * { margin: 0; padding: 0; box-sizing: border-box; }
  html, body {
    width: 1200px;
    height: 900px;
    overflow: hidden;
    background: var(--backdrop);
  }
  .canvas {
    position: relative;
    width: 1200px;
    height: 900px;
    background: var(--backdrop);
  }
  .card-cover {
    position: absolute;
    left: 180px;
    top: 150px;
    width: 839px;
    height: 598px;
    background: var(--card-red);
    overflow: hidden;
  }
  .thanks-tag {
    position: absolute;
    left: 379px;
    top: 417px;
    width: 360px;
    height: 205px;
    transform-origin: 0 0;
    transform: rotate(-13.6deg);
  }
  .tag-panel {
    position: absolute;
    left: 0;
    top: 0;
    width: 100%;
    height: 168px;
    background: var(--tag-taupe);
  }
  .tag-script {
    position: absolute;
    left: 44px;
    top: 4px;
    font-family: "Pinyon Script", cursive;
    font-size: 118px;
    line-height: 1;
    color: var(--script-cream);
    white-space: nowrap;
  }
  .tag-band {
    position: absolute;
    left: 0;
    top: 168px;
    width: 100%;
    height: 37px;
    background: var(--tag-lime);
  }
  .tag-caption {
    position: absolute;
    right: 36px;
    top: 4px;
    font-family: "Archivo", Arial, sans-serif;
    font-weight: 500;
    font-size: 17px;
    letter-spacing: 0.32em;
    color: var(--caption-ink);
    white-space: nowrap;
  }
</style>
</head>
<body>
  <main class="canvas">
    <section class="card-cover">
      <div class="thanks-tag">
        <div class="tag-panel">
          <span class="tag-script">Thanx</span>
        </div>
        <div class="tag-band">
          <span class="tag-caption">for the Referral</span>
        </div>
      </div>
    </section>
  </main>
</body>
</html>
```